Web-Design  für naturwissenschaflich-philosophische Institution
Zielgruppe
Es handelt sich um eine naturwissenschaflich-philosophische Institution. Besucher sind neben Natur- und Geisteswissenschaftlern auch interessierte Laien.
Kernthema der Seite ist alles rund um das Thema Zahlen, allerdings unter einem naturwissenschaftlich, philosophischen Aspekt. Nach einer grundsätzlichen Erklärung (Leitartikel 'Als Flüsse singen') baut die Seite sich auf aus zahreichen Beispielen/Beiträgen aus den unterschiedlichsten Fachbereichen, die scheinbar keinerlei Bezug zueinander haben, wie Mathematik, Geometrie einerseits und der großen Literatur einschließlich historischer und religiöser Schriften andererseits. Immer aber gibt es einen Bezug zu fraktal wachsenden Dreiecken.
Die Artikel sind meist populärwissenschaftlich formuliert. Es handelt sich nicht um esoterische Inhalte, auch wenn der Domainname www.kelmbrauth.de das evtl. vermuten ließe. Keine Berührung zu Spiritualität. Die Institution ist im Aufbau und hat durchaus den Anspruch, diese klassischen Themen modern aufzugreifen. Sie ist nicht verstaubt.
Aufgabenstellung
Geordneter, klarer, transparenter Aufbau. Übersichtlich und strukturiert, wie zB www.qrl.de Es sollten geometrische Proportionen eingehalten werden (wie Symmetrie, goldener Schnitt). Nicht zu viele verschiedene Stilelemente. Die Seite sollte einladend sein, ggf. ansprechendes Bild auf Startseite (mit Bezug zu Zahlen, Geoemetrie).
Die Startseite braucht nun im Header kein Logo mehr zu haben. Der Seitentitel sollte sein 'Das Echo der Wolken'. Siehe Anhang 'Header Beispiel'
Als Menüpunkte benötigen wir neben Home, nur 'Beiträge', 'Buch', 'Kontakt' oder einfach nur die bekannten drei Striche. Der Link zum Impressum genügt im Footer. Rechts oben benötigt man ein Suchfeld.
Besonderheit: Man benötigt eine Art zweiten Header, der aus einer Zahlenreihe besteht. Die einzelnen Zahlen müssen später verlinkt sein auf Unterseiten. Siehe Muster im Anhang. Der User muss sie als Link erkennen können (evtl. Programmierthema: zB Hervorheben beim drüberhoovern). Die Zahlen müssen erweiterbar sein, ggf. über Pfeil klicken, siehe
Es gibt einen zentralen Startartikel. Auf diesen muss man leicht kommen. Im Muster heißt er 'Als die Flüsse singen'.
Das Bild hier ist sehr wichtig. Es sollte bestehn aus vielen interessanten Zahlen, wie in 'Zahlenwolke' angegeben. Und möglichst auch den Dreiecken wie in 'Logo1'.
Weiter unten auf der Startseite sollte es dann weitere Elemente geben, einmal wo man zu bestimmten Unterkategorien kommt, im Muster sind das 'Bibel und Zahlen' 'Naturwissenschaft' etc. und dann evtl weiter unten noch ein Stilelemente, in welchem man die neuesten Artikel verlinken kann.

```html
<!DOCTYPE html>
<html lang="de">
<head>
<meta charset="utf-8">
<title>Das Echo der Wolken</title>
<link rel="stylesheet" href="https://fonts.googleapis.com/css2?family=Poppins:wght@400;500;600;700&display=swap">
<style>
:root{
  --blue:#1488fc;
  --ink:#22354d;
  --paper:#ffffff;
  --mist:#ededed;
  --card:#f1f1f1;
  --line:#c9c9c9;
}
*{box-sizing:border-box;margin:0;padding:0}
html,body{width:1153px;height:1200px;overflow:hidden}
body{font-family:"Poppins",sans-serif;background:var(--paper);color:var(--ink);position:relative}
.site-header{position:absolute;left:0;top:0;width:1153px;height:60px;background:var(--paper);z-index:2;box-shadow:0 1px 3px rgba(0,0,0,.08)}
.site-title{position:absolute;left:169px;top:16px;font-size:20px;font-weight:400;color:var(--blue);letter-spacing:.2px}
.site-title b{font-weight:600}
.main-nav{position:absolute;left:520px;top:23px;display:flex;align-items:center;font-size:10.5px;font-weight:500;letter-spacing:.3px}
.main-nav a{color:var(--ink);text-decoration:none;padding:0 12px;border-left:1px solid var(--line);line-height:11px}
.main-nav a:first-child{padding-left:0;border-left:none;color:var(--blue);position:relative}
.main-nav a:first-child::after{content:"";position:absolute;left:0;right:12px;bottom:-7px;height:2px;background:var(--blue)}
.search{position:absolute;left:864px;top:18px;width:121px;height:24px;border:1px solid #9aa3ad;border-radius:2px;font-size:10px;color:#d0d4d8;padding:5px 6px}
.search svg{position:absolute;right:6px;top:5px}
.number-bar{position:absolute;left:0;top:60px;width:1153px;height:36px;background:var(--mist);box-shadow:0 2px 4px rgba(0,0,0,.08);z-index:1}
.number-bar .label{position:absolute;left:598px;top:11px;font-size:10.5px;font-weight:500}
.number-bar .arrow{position:absolute;top:14px;width:0;height:0;border-top:3.5px solid transparent;border-bottom:3.5px solid transparent}
.arrow.prev{left:740px;border-right:5px solid var(--ink)}
.arrow.next{left:980px;border-left:5px solid var(--blue)}
.numbers{position:absolute;left:757px;top:9px;display:flex;gap:6px}
.numbers a{width:18px;height:18px;border-radius:3px;background:var(--ink);color:#fff;font-size:13px;font-weight:600;text-align:center;line-height:19px;text-decoration:none}
.numbers a.active{background:var(--blue)}
.hero{position:absolute;left:0;top:96px;width:1153px;height:504px;background:var(--mist)}
.hero h1{position:absolute;left:169px;top:155px;font-size:55px;line-height:61px;font-weight:700;letter-spacing:-.5px;color:var(--ink)}
.btn{display:block;background:var(--blue);color:#fff;font-size:11px;font-weight:500;text-align:center;text-decoration:none}
.hero .btn{position:absolute;left:169px;top:305px;width:220px;height:36px;line-height:36px}
.hero-figure{position:absolute;left:646px;top:62px;width:424px;height:381px;clip-path:polygon(50% 0,100% 100%,0 100%);background:linear-gradient(160deg,#cfe5fb,#8fc3f7 60%,#5fa9f5)}
.topics{position:absolute;left:169px;top:690px;display:flex;gap:23px}
.topic{width:257px;height:300px;background:var(--card);box-shadow:0 1px 4px rgba(0,0,0,.1);padding:26px 25px 0;position:relative}
.topic h2{font-size:28px;line-height:34px;font-weight:600;height:80px}
.topic p{margin-top:4px;font-size:11px;line-height:15.6px;font-weight:400;color:#333d48}
.topic .btn{position:absolute;left:25px;top:240px;width:134px;height:36px;line-height:36px}
.to-top{position:absolute;left:1045px;top:1092px;width:24px;height:24px;background:#e6e6e6;border-radius:2px}
.to-top::after{content:"";position:absolute;left:6px;top:7px;border-left:6px solid transparent;border-right:6px solid transparent;border-bottom:10px solid var(--ink)}
.site-footer{position:absolute;left:0;top:1138px;width:1153px;height:62px;background:var(--mist);box-shadow:0 -2px 4px rgba(0,0,0,.05)}
</style>
</head>
<body>
<header class="site-header">
  <div class="site-title"><b>Das Echo</b> der Wolken</div>
  <nav class="main-nav">
    <a href="#">HOME</a><a href="#">BETRAGE</a><a href="#">BUCH</a><a href="#">KONTAKT</a><a href="#">IMPRESSUM</a>
  </nav>
  <div class="search">Suche
    <svg width="12" height="12" viewBox="0 0 12 12"><circle cx="7" cy="5" r="3.8" fill="none" stroke="#22354d" stroke-width="1.2"/><line x1="4.3" y1="7.7" x2="1" y2="11" stroke="#22354d" stroke-width="1.2"/></svg>
  </div>
</header>
<div class="number-bar">
  <span class="label">und was sie erzählen:</span>
  <span class="arrow prev"></span>
  <div class="numbers">
    <a class="active" href="#">1</a><a href="#">2</a><a href="#">3</a><a href="#">4</a><a href="#">5</a><a href="#">6</a><a href="#">7</a><a href="#">8</a><a href="#">9</a>
  </div>
  <span class="arrow next"></span>
</div>
<section class="hero">
  <h1>Als die<br>Flüsse singen ...</h1>
  <a class="btn" href="#">Lern mehr</a>
  <div class="hero-figure" role="img" aria-label="Großes, fraktal geteiltes Zahlendreieck aus kleineren nummerierten Dreiecken in Blau"></div>
</section>
<section class="topics">
  <article class="topic">
    <h2>Bibel und Zahlen</h2>
    <p>Die Heilige Schrift ist ein Werk aus Zahlen. Ihre Verfasser haben die archetypischen Inhalte in wundersamer Art und Weise in der Bibel. Und so weiter und so fort</p>
    <a class="btn" href="#">Lern mehr</a>
  </article>
  <article class="topic">
    <h2>Naturwissens chaft</h2>
    <p>Die Heilige Schrift ist ein Werk aus Zahlen. Ihre Verfasser haben die archetypischen Inhalte in wundersamer Art</p>
    <a class="btn" href="#">Lern mehr</a>
  </article>
  <article class="topic">
    <h2>Philosophie</h2>
    <p>Die Heilige Schrift ist ein Werk aus Zahlen. Ihre Verfasser haben die archetypischen Inhalte in wundersamer Art und Weise der Bibel. Und so weiter und so fort und vieles mehr das sehr schön eindrucksvoll ist</p>
    <a class="btn" href="#">Lern mehr</a>
  </article>
</section>
<a class="to-top" href="#" aria-label="Nach oben"></a>
<footer class="site-footer"></footer>
</body>
</html>
```